Website on Hubspot CMS -Boutique consulting firm focused on the events and event tech industries

Design website for our business using Hubspot CMS. Some pages already done. We would like those tweaked to match your recommended design. We also would like landing pages created for four business services offerings. We have a color palette and logo.

Our current website can be found here: www.qlvadvisors.co

QLV Advisors has four service lines:
1. Outsourced Sales
2. Harbor Ledger Strategic Consulting
3. Gridweave Strategic Consulting
4. QLV VIP

Target Market(s)

event organizers, media companies, corporate event marketers, event tech organizations

Industry/Entity Type

Consulting

Coding

Coded - Design and coding required

Number of Pages Required

5+ page

Font styles to use
Sans Serif

Requirements
Must have
• This will be a website built using Hubspot CMS. If you are not familiar with this, please do not participate as we will not be able to use your designs.
SEO optimized
Landing pages with lead capture leading to content downloads
Each service line needs its own page/s with cta's
Highly visual, modern, bold
Navigational areas: Home, Services, Resources, Events, Blog, About Us
Content formats: video, podcasts, content downloads
Will need at least 4 landing pages in addition to the website for each service line plus templates in case we need to update with new copy
We have or own color palette and logo as well as logos for Harbor Ledger and Gridweave. Those colors must be used.
Font can be modified
We need to have a conversation with the designer that is chosen to go over each service line and also understand what kind of images we should be uploading.
Nice to have
• We would really like the site to reflect the following words:
Bold
Future focused
Results oriented
Hyper focused on the events and event technology sectors (sub sectors: corporate event marketers and B2B media companies).
Should not have
• Flat one page design

```html
<!DOCTYPE html>
<html lang="en">
<head>
<meta charset="utf-8">
<title>QLV Advisors</title>
<link href="https://fonts.googleapis.com/css2?family=Roboto:wght@400;500;700&display=swap" rel="stylesheet">
<style>
:root{
  --brand:#ff4a0b;
  --ink:#222;
  --muted:#555;
  --line:#ddd;
  --field:#f6f6f6;
  --footer:#333;
}
*{box-sizing:border-box;margin:0;padding:0}
html,body{width:1200px;height:3567px;overflow:hidden}
body{font-family:"Roboto",Arial,sans-serif;color:var(--ink);background:#fff;position:relative}
.abs{position:absolute}
/* header */
.site-header{position:absolute;left:0;top:0;width:1200px;height:137px;background:#fff}
.brand-name{position:absolute;left:111px;top:40px;font-size:40px;font-weight:500;color:var(--brand);white-space:nowrap}
.nav{position:absolute;top:60px;font-size:14px;font-weight:500;color:#333}
.nav a{position:absolute;white-space:nowrap;text-decoration:none;color:inherit}
.nav a.active{color:var(--brand)}
/* hero */
.hero{position:absolute;left:0;top:137px;width:1200px;height:721px;background:linear-gradient(120deg,#6d6a66 0%,#8d847c 35%,#a39a90 55%,#5c5853 100%)}
.hero-shade{position:absolute;inset:0;background:linear-gradient(90deg,rgba(0,0,0,.35),rgba(0,0,0,.05))}
.hero h1{position:absolute;left:110px;top:313px;font-size:59px;font-weight:500;color:#fff}
.hero .tagline{position:absolute;left:110px;top:400px;font-size:34px;line-height:49px;color:#fff}
.hero .tagline sup{font-size:15px}
.btn{position:absolute;background:var(--brand);color:#fff;font-size:16px;text-align:center;border-radius:3px}
.hero .btn{left:111px;top:516px;width:146px;height:50px;line-height:50px}
.request-card{position:absolute;left:747px;top:134px;width:343px;height:451px;background:#fff;border-radius:14px}
.request-card h2{text-align:center;margin-top:27px;font-size:25px;font-weight:700}
.request-card .lead{text-align:center;font-size:13px;color:var(--muted);margin-top:10px}
.field-label{position:absolute;left:30px;font-size:12px;color:#666}
.field{position:absolute;left:30px;width:284px;height:48px;background:var(--field);border:1px solid #e6e6e6;box-shadow:0 2px 4px rgba(0,0,0,.1)}
.request-card .btn{left:30px;top:375px;width:284px;height:46px;line-height:46px;font-weight:500;font-size:17px}
/* services */
.section-title{position:absolute;left:0;width:1200px;text-align:center;font-size:36px;color:#333}
.title-rule{position:absolute;left:577px;top:972px;width:47px;height:3px;background:var(--brand)}
.service{position:absolute;left:0;width:1200px;height:420px}
.svc-frame{position:absolute;width:473px;height:303px;background:var(--brand)}
.svc-photo{position:absolute;width:472px;height:310px}
.svc-card{position:absolute;top:35px;width:100px;height:235px;background:#fff}
.svc-title{position:absolute;font-size:25px;font-weight:500;color:#333;white-space:nowrap}
.svc-text{position:absolute;width:478px;font-size:13.5px;line-height:25.6px;color:var(--muted);text-align:justify}
.learn{position:absolute;font-size:15px;color:var(--brand);text-decoration:underline;white-space:nowrap}
.learn svg{vertical-align:middle;margin-left:4px}
/* testimonials */
.testimonials{position:absolute;left:0;top:2686px;width:1200px;height:370px;background:var(--brand);color:#fff}
.avatar{position:absolute;width:140px;height:140px;border-radius:50%;border:3px solid #fff}
.t-name{position:absolute;font-size:23px;font-weight:500}
.t-role{position:absolute;font-size:17px}
.stars{position:absolute;font-size:14px;letter-spacing:2px}
.t-text{position:absolute;width:教;font-size:13px;line-height:29px;text-align:justify}
/* contact */
.contact-sub{position:absolute;left:0;top:3169px;width:1200px;text-align:center;font-size:16px;color:#333}
.contact-brand{position:absolute;left:270px;top:3320px;font-size:50px;font-weight:500;color:var(--brand);white-space:nowrap}
.contact-divider{position:absolute;left:612px;top:3243px;width:1px;height:185px;background:var(--line)}
.c-icon{position:absolute;left:684px;width:42px;height:42px;border:2px solid var(--brand);border-radius:50%}
.c-icon svg{position:absolute;left:10px;top:10px}
.c-label{position:absolute;left:749px;font-size:15px;font-weight:500;color:#444}
.c-value{position:absolute;left:749px;font-size:12px;color:#555}
/* footer */
.site-footer{position:absolute;left:0;top:3479px;width:1200px;height:88px;background:var(--footer);color:#fff}
.site-footer .copy{position:absolute;left:112px;top:36px;font-size:15px}
.social{position:absolute;top:25px;width:42px;height:42px;border:2px solid #fff;border-radius:50%}
</style>
</head>
<body>

<header class="site-header">
  <div class="brand-name">QLV Advisors</div>
  <nav class="nav">
    <a class="active" style="left:480px">HOME</a>
    <a style="left:574px">SERVICES</a>
    <a style="left:692px">RESOURCES</a>
    <a style="left:825px">EVENTS</a>
    <a style="left:930px">BLOG</a>
    <a style="left:1020px">ABOUT US</a>
  </nav>
</header>

<section class="hero" role="img" aria-label="Two smiling colleagues working together at a laptop in a bright office">
  <div class="hero-shade"></div>
  <h1>QLV Advisors</h1>
  <p class="tagline">Modernize Your Harbor Ledger<sup>™</sup><br>Get More Customers.</p>
  <a class="btn">READ MORE</a>
  <form class="request-card">
    <h2>GET REQUEST</h2>
    <p class="lead">Simply dummy text of the printing</p>
    <span class="field-label" style="top:108px">First Name</span>
    <div class="field" style="top:130px"></div>
    <span class="field-label" style="top:194px">Last Name</span>
    <div class="field" style="top:216px"></div>
    <span class="field-label" style="top:280px">Email</span>
    <div class="field" style="top:302px"></div>
    <div class="btn">SUBMIT</div>
  </form>
</section>

<h2 class="section-title" style="top:920px">OUR SERVICES</h2>
<div class="title-rule"></div>

<!-- service 1 -->
<article class="service" style="top:1042px">
  <div class="svc-frame" style="left:111px;top:21px"></div>
  <div class="svc-photo" style="left:125px;top:0;background:linear-gradient(120deg,#c9d0d6,#8d97a0 50%,#e3e6e8)" role="img" aria-label="Hand touching a digital outsourcing interface with network icons"></div>
  <div class="svc-card" style="left:537px;width:563px"></div>
  <h3 class="svc-title" style="left:579px;top:72px">Outsourced Sales</h3>
  <p class="svc-text" style="left:581px;top:124px">We offer outsourced sales leadership, individual contributor and customer success support for event tech, event organizations, and associations who have rapid go-to-market demands with a new product launch, resource gaps, or who are entering a new geographic market.</p>
  <a class="learn" style="left:944px;top:241px">LEARN MORE<svg width="20" height="10" viewBox="0 0 20 10"><path d="M0 5H18M13 1l5 4-5 4" stroke="#ff4a0b" stroke-width="2" fill="none"/></svg></a>
</article>

<!-- service 2 -->
<article class="service" style="top:1457px">
  <div class="svc-frame" style="left:617px;top:21px"></div>
  <div class="svc-photo" style="left:605px;top:0;background:linear-gradient(135deg,#0d1f3c,#28476f 50%,#0b1830)" role="img" aria-label="Businessman behind a glowing world network map"></div>
  <div class="svc-card" style="left:100px;width:553px"></div>
  <h3 class="svc-title" style="left:143px;top:72px">Harbor Ledger Strategic Consulting</h3>
  <p class="svc-text" style="left:145px;top:124px">We work with customers to map out profitable digital strategies to complement and enhance live events. Our expertise lies in identifying new revenue streams that allow for superior customer experience, greater share of wallet longer value and better customer retention and expansion.</p>
  <a class="learn" style="left:509px;top:241px">LEARN MORE<svg width="20" height="10" viewBox="0 0 20 10"><path d="M0 5H18M13 1l5 4-5 4" stroke="#ff4a0b" stroke-width="2" fill="none"/></svg></a>
</article>

<!-- service 3 -->
<article class="service" style="top:1871px">
  <div class="svc-frame" style="left:111px;top:21px"></div>
  <div class="svc-photo" style="left:125px;top:0;background:linear-gradient(120deg,#8b8a80,#cbb98a 55%,#e7d9a8)" role="img" aria-label="Team collaborating around a glass wall with sticky notes"></div>
  <div class="svc-card" style="left:537px;width:563px"></div>
  <h3 class="svc-title" style="left:579px;top:72px">Gridweave Strategic Consulting</h3>
  <p class="svc-text" style="left:581px;top:124px">We offer outsourced sales leadership, individual contributor and customer success support for event tech, event organizations, and associations who have rapid go-to-market demands with a new product launch, resource gaps, or who are entering a new geographic market.</p>
  <a class="learn" style="left:944px;top:241px">LEARN MORE<svg width="20" height="10" viewBox="0 0 20 10"><path d="M0 5H18M13 1l5 4-5 4" stroke="#ff4a0b" stroke-width="2" fill="none"/></svg></a>
</article>

<!-- service 4 -->
<article class="service" style="top:2285px">
  <div class="svc-frame" style="left:617px;top:21px"></div>
  <div class="svc-photo" style="left:605px;top:0;background:linear-gradient(135deg,#e6e8ec,#6f86a8 45%,#1d3766)" role="img" aria-label="Businessman typing on a laptop with glowing data overlay"></div>
  <div class="svc-card" style="left:100px;width:553px"></div>
  <h3 class="svc-title" style="left:143px;top:72px">QLV VIP</h3>
  <p class="svc-text" style="left:145px;top:124px">We model and roll out 21st century sales organizations designed to meet our clients’ new customer demands. We work with clients to navigate today’s more complex selling environment and adapt and upskill teams quickly in order to capture more wallet-share and increase LTV of their customers.</p>
  <a class="learn" style="left:509px;top:241px">LEARN MORE<svg width="20" height="10" viewBox="0 0 20 10"><path d="M0 5H18M13 1l5 4-5 4" stroke="#ff4a0b" stroke-width="2" fill="none"/></svg></a>
</article>

<section class="testimonials">
  <div class="avatar" style="left:112px;top:36px;background:linear-gradient(160deg,#e9d9b8,#b7946e)" role="img" aria-label="Portrait of client Mara Kestrel"></div>
  <div class="t-name" style="left:275px;top:61px">Mara Kestrel</div>
  <div class="t-role" style="left:275px;top:95px">CEO / Fennrow</div>
  <div class="stars" style="left:277px;top:127px">☆☆☆☆☆</div>
  <p class="t-text" style="left:112px;top:192px;width:425px">Mara worked with Fennrow for 16 months, helping to build and strengthen our profile in the US. She showed us how we could better expand our business, taught us fundamental sales practice and helped to identify where our product gaps were.</p>

  <div class="avatar" style="left:657px;top:36px;background:linear-gradient(160deg,#d9d9d9,#8c8c8c)" role="img" aria-label="Portrait of client Dorian Vale"></div>
  <div class="t-name" style="left:821px;top:61px">Dorian Vale</div>
  <div class="t-role" style="left:821px;top:95px">CEO &amp; Co-Founder/ Tidepoint</div>
  <div class="stars" style="left:823px;top:127px">☆☆☆☆☆</div>
  <p class="t-text" style="left:657px;top:192px;width:431px">Thank you again for the excellent class and also for the specific insights during our 1:1 session.It was hands down the best sales course we have taken, and your feedback came just in time for our conference and meeting with a potential sales hire.</p>
</section>

<h2 class="section-title" style="top:3107px">CONTACT US</h2>
<p class="contact-sub">Reach out to us to find out how we can help you achieve your growth objectives.</p>
<div class="contact-brand">QLV Advisors</div>
<div class="contact-divider"></div>

<div class="c-icon" style="top:3252px"><svg width="18" height="18" viewBox="0 0 18 18"><path d="M9 1a6 6 0 0 0-6 6c0 4.5 6 10 6 10s6-5.5 6-10a6 6 0 0 0-6-6z" fill="#ff4a0b"/><circle cx="9" cy="7" r="2" fill="#fff"/></svg></div>
<div class="c-label" style="top:3256px">ADDRESS</div>
<div class="c-value" style="top:3278px">44 Lorem Ipsum Dummy lorem</div>

<div class="c-icon" style="top:3317px"><svg width="18" height="18" viewBox="0 0 18 18"><path d="M4 2l3 3-1.5 2a9 9 0 0 0 5.5 5.5L13 11l3 3-2 2C8 16 2 10 2 4z" fill="#ff4a0b"/></svg></div>
<div class="c-label" style="top:3320px">PHONE</div>
<div class="c-value" style="top:3342px">555 014 2288</div>

<div class="c-icon" style="top:3384px"><svg width="18" height="18" viewBox="0 0 18 18"><rect x="1" y="4" width="16" height="11" rx="1" fill="#ff4a0b"/><path d="M1 5l8 6 8-6" stroke="#fff" stroke-width="1.5" fill="none"/></svg></div>
<div class="c-label" style="top:3385px">EMAIL</div>
<div class="c-value" style="top:3407px">hello@qlvadvisors.co</div>

<footer class="site-footer">
  <p class="copy">Copyright ©2021. All rights reserved. | Privacy Policy</p>
  <span class="social" style="left:905px" aria-label="Social link"></span>
  <span class="social" style="left:953px" aria-label="Social link"></span>
  <span class="social" style="left:1001px" aria-label="Social link"></span>
  <span class="social" style="left:1049px" aria-label="Social link"></span>
</footer>

</body>
</html>
```